Web Developer Wordpress theme

I'm a web developer but a poor designer so i need somebody to design me a cool and professional WordPress theme. I specialize in shopping cart developments and modifications as well as hosting for these system so would like the design to show this off. I am UK based and want this to also come across in the design.
As for colors and layout i am open mined just use your imaginantion i will let know what i think of your designs.
also forgot to mention my business name is vartelux
and my exsiting site is vartelux.co.uk

```html
<!DOCTYPE html>
<html lang="en">
<head>
<meta charset="utf-8">
<title>Vartelux – Serious Web Development</title>
<link rel="stylesheet" href="https://fonts.googleapis.com/css2?family=Abel&family=Arimo:wght@400;700&display=swap">
<style>
:root{
  --orange:#f38a12;
  --orange-dark:#d86a00;
  --blue:#1a6fc0;
  --blue-dark:#0d4f95;
  --ink:#1d1d1d;
  --panel:#2f2f2f;
  --panel-edge:#4a4a4a;
  --muted:#b8b8b8;
  --light:#e9e9e9;
  --white:#ffffff;
}
*{box-sizing:border-box;margin:0;padding:0}
html,body{width:937px;height:1200px;overflow:hidden}
body{position:relative;background:var(--light);font-family:"Arimo",Arial,sans-serif;color:var(--ink)}
.abs{position:absolute}
.header{left:0;top:0;width:937px;height:117px;background:linear-gradient(#fafafa,#e4e4e4)}
.brand{left:27px;top:22px;font-size:44px;font-weight:700;color:var(--orange);letter-spacing:-1px;line-height:1}
.brand-dot{display:inline-block;width:26px;height:26px;background:var(--blue);border-radius:50%;margin-right:8px;vertical-align:middle}
.tagline{left:100px;top:86px;font-size:10px;letter-spacing:2px;color:#555}
.contact{right:26px;top:18px;text-align:right;font-size:12px;color:#555;line-height:18px}
.contact svg{position:absolute;left:-40px;top:4px}
.nav{right:26px;top:72px;display:flex;gap:22px;align-items:center;font-size:14px}
.nav a{color:#111;text-decoration:none}
.nav .current{background:linear-gradient(var(--blue),var(--blue-dark));color:var(--white);padding:5px 12px;border-radius:3px}
.hero{left:0;top:117px;width:937px;height:563px;background:linear-gradient(#1b1b1b,#111 70%,#222)}
.hero-photo{left:540px;top:117px;width:397px;height:353px;background:radial-gradient(circle at 55% 55%,#c89a12 0,#6b5416 22%,#262626 55%,#151515)}
.hero-title{left:64px;top:188px;font-family:"Abel",sans-serif;font-size:31px;color:var(--orange)}
.hero-text{left:36px;top:244px;width:390px;font-size:11.5px;line-height:15.5px;color:var(--muted);text-align:justify}
.btn-dark{left:256px;top:368px;width:161px;height:48px;border-radius:5px;background:linear-gradient(#4a4a4a,#1e1e1e);border:1px solid #555;color:#eee;font-family:"Abel",sans-serif;font-size:22px;display:flex;align-items:center;justify-content:center}
.label{font-family:"Abel",sans-serif;font-size:19px}
.slider{left:27px;top:526px;width:572px;height:204px;border-radius:10px;background:linear-gradient(#3a3a3a,#2a2a2a 60%,#d5d5d5);box-shadow:0 2px 6px rgba(0,0,0,.4)}
.thumb{top:544px;width:152px;height:162px;border-radius:6px;border:2px solid #fff}
.arrow{top:592px}
.welcome{left:618px;top:528px;width:290px;height:42px;background:linear-gradient(90deg,#3c3c3c,#1d1d1d);font-family:"Abel",sans-serif;font-size:27px;color:#f2c27a;padding:4px 12px}
.welcome-text{left:626px;top:580px;width:276px;font-size:12px;line-height:16px;color:#ddd;text-align:justify}
.btn-blue{left:758px;top:657px;width:130px;height:38px;background:linear-gradient(#2d8de0,var(--blue-dark));color:#fff;font-family:"Abel",sans-serif;font-size:20px;display:flex;align-items:center;justify-content:center;box-shadow:0 4px 5px rgba(0,0,0,.3)}
.services{left:30px;top:785px;width:878px;height:345px;border-radius:10px;background:var(--panel);border:3px solid #d6d6d6}
.service-title{top:803px;font-family:"Abel",sans-serif;font-size:18px;color:#eee}
.service-card{top:834px;width:260px;height:265px;border-radius:8px;background:linear-gradient(#1e1e1e,#3a3a3a);border:1px solid var(--panel-edge)}
.service-img{position:absolute;left:18px;top:16px;width:222px;height:113px;border-radius:5px}
.service-text{position:absolute;left:18px;top:150px;width:224px;font-size:10.5px;line-height:15.5px;color:#ccc}
.btn-detail{position:absolute;left:154px;top:246px;width:70px;height:26px;background:linear-gradient(#ffa43a,var(--orange-dark));color:#222;font-size:15px;display:flex;align-items:center;justify-content:center}
.footer{left:0;top:1138px;width:937px;height:62px;background:#f3f3f3}
.footer-brand{left:58px;top:1150px;font-size:26px;font-weight:700;color:var(--orange)}
.footer-links{left:186px;top:1155px;font-size:10.5px;color:#333}
.footer-links a{color:#333;text-decoration:none;margin:0 6px}
.footer-links a:first-child{color:var(--blue);margin-left:0}
.copy{left:186px;top:1174px;font-size:10.5px;color:#333}
.social{top:1153px;width:34px;height:34px;border-radius:50%;background:linear-gradient(#9a9a9a,#555)}
</style>
</head>
<body>
<header class="abs header"></header>
<div class="abs brand"><span class="brand-dot"></span>vartelux</div>
<div class="abs tagline">serious web developement</div>
<div class="abs contact">
  <svg width="30" height="22" viewBox="0 0 30 22"><path d="M3 6 Q15 -2 27 6 L24 10 L19 8 L19 6 Q15 4 11 6 L11 8 L6 10Z" fill="#4a7fb8"/><rect x="6" y="10" width="18" height="11" rx="2" fill="#4a7fb8"/></svg>
  020 7946 0321<br>hello@vartelux.co.uk
</div>
<nav class="abs nav"><a class="current" href="#">Home</a><a href="#">About Us</a><a href="#">Work</a><a href="#">Contact Us</a></nav>

<section class="abs hero"></section>
<div class="abs hero-photo" role="img" aria-label="Keyboard with a yellow add-to-cart key and a shopping trolley"></div>
<h1 class="abs hero-title" style="font-weight:400">Our E-Commerce Hosting</h1>
<p class="abs hero-text">Lorem ipsum dolor sit amet, consectetur adipiscing elit. Nam vitae interdum libero. Aliquam gravida fringilla iaculis. Nam vehicula, mauris sollicitudin pellentesque ullamcorper, lacus orci faucibus nulla, sed egestas nibh mauris at nunc. Duis semper arcu dolor. Integer vitae erat enim. Duis semper arcu dolor. Integer vitae erat enim. Duis semper arcu dolor. Integer vitae erat enim.</p>
<div class="abs btn-dark">SEE SERVERS</div>

<h2 class="abs label" style="left:26px;top:490px;color:#fff;font-weight:400">Recent Projects</h2>
<div class="abs slider"></div>
<svg class="abs arrow" style="left:48px" width="12" height="62" viewBox="0 0 12 62"><path d="M10 2 L2 31 L10 60" stroke="var(--orange)" stroke-width="2.5" fill="none"/></svg>
<svg class="abs arrow" style="left:562px" width="12" height="62" viewBox="0 0 12 62"><path d="M2 2 L10 31 L2 60" stroke="var(--orange)" stroke-width="2.5" fill="none"/></svg>
<div class="abs thumb" style="left:76px;background:linear-gradient(#e8e8e8,#a9b3b8)" role="img" aria-label="Magnifying glass over a keyboard"></div>
<div class="abs thumb" style="left:236px;background:linear-gradient(#5a5f66,#2a2c30)" role="img" aria-label="Tablet showing a social media diagram"></div>
<div class="abs thumb" style="left:396px;background:linear-gradient(#f4f4f4,#c9d4e6)" role="img" aria-label="Shopping cart filled with colourful app icons"></div>

<h2 class="abs welcome" style="font-weight:400">Welcome to our site</h2>
<p class="abs welcome-text">Lorem ipsum dolor sit amet, consectetur adipiscing elit. Nam vitae interdum libero. Aliquam gravida fringilla iaculis. Nam vehicula, mauris sollicitudin pellentesque ullamcorper, lacus orci</p>
<div class="abs btn-blue">Read More</div>

<h2 class="abs label" style="left:26px;top:752px;color:#222;font-weight:400">Services</h2>
<section class="abs services"></section>

<h3 class="abs service-title" style="left:78px;font-weight:400">Web Developement</h3>
<div class="abs service-card" style="left:61px">
  <div class="service-img" style="background:radial-gradient(#d9e8f8,#fff)" role="img" aria-label="Blue flowchart blocks"></div>
  <p class="service-text">Lorem ipsum dolor sit amet, consectetur adipiscing elit. Phasellus et sapien id neque posuere pharetra eu ac urna. Quisque aliquam vulputate elit, sit amet tempor quam lacinia at. Sed ullamcorper, ipsum eu dapibus commodo,</p>
  <div class="btn-detail">Detail</div>
</div>

<h3 class="abs service-title" style="left:357px;font-weight:400">Shopping Cart Maintenance</h3>
<div class="abs service-card" style="left:340px">
  <div class="service-img" style="background:radial-gradient(#f0d0d0,#fff 70%)" role="img" aria-label="Red toolbox figure pushing a shopping cart"></div>
  <p class="service-text">Lorem ipsum dolor sit amet, consectetur adipiscing elit. Phasellus et sapien id neque posuere pharetra eu ac urna. Quisque aliquam vulputate elit, sit amet tempor quam lacinia at. Sed ullamcorper, ipsum eu dapibus commodo,</p>
  <div class="btn-detail">Detail</div>
</div>

<h3 class="abs service-title" style="left:636px;font-weight:400">Shopping Cart Hosting</h3>
<div class="abs service-card" style="left:619px">
  <div class="service-img" style="background:radial-gradient(#cfe6f3,#fff 70%)" role="img" aria-label="Blue circular process cycle with icons"></div>
  <p class="service-text">Lorem ipsum dolor sit amet, consectetur adipiscing elit. Phasellus et sapien id neque posuere pharetra eu ac urna. Quisque aliquam vulputate elit, sit amet tempor quam lacinia at. Sed ullamcorper, ipsum eu dapibus commodo,</p>
  <div class="btn-detail">Detail</div>
</div>

<footer class="abs footer"></footer>
<div class="abs footer-brand">vartelux</div>
<nav class="abs footer-links"><a href="#">Home</a>|<a href="#">About Us</a>|<a href="#">Work</a>|<a href="#">Privacy Policy</a></nav>
<div class="abs copy">CopyRights 2012.All Rights Reserved</div>
<div class="abs social" style="left:760px;background:linear-gradient(#ffa43a,var(--orange-dark))">
  <svg width="34" height="34" viewBox="0 0 34 34"><rect x="9" y="11" width="16" height="12" rx="1" fill="#fff"/><path d="M9 12 L17 18 L25 12" stroke="#d86a00" stroke-width="1.5" fill="none"/></svg>
</div>
<div class="abs social" style="left:800px"></div>
<div class="abs social" style="left:842px"></div>
</body>
</html>
```